Bref créative
Saltmarsh Restaurant
Truly Island-Made
Simple
#41 Estate Coralind
(at the Harbor Bluff Cottages)
Christiansted, VI 00820
Saltmarsh_Restaurant@bayvistamail.com
www.saltmarshvi-example.com
* Free Wi-fi
* Special events venue-mediations, meetings, fund raisers, wedding receptions, catering, private parties, you name it we can host it !!
* Superior customer service
* Delicious cuisine
please use this logo

```html
<!DOCTYPE html>
<html lang="en">
<head>
<meta charset="utf-8">
<title>Saltmarsh Restaurant – Business Cards</title>
<link href="https://fonts.googleapis.com/css2?family=Arimo:wght@400;700&display=swap" rel="stylesheet">
<style>
:root{
  --stage:#5b5c5e;
  --paper:#f7f7f7;
  --paper-shade:#e6e7e8;
  --ink:#1f1f1f;
  --ink-soft:#4a4a4a;
  --night:#262626;
  --night-light:#3e3e3e;
  --sea:#a9ddd8;
  --sea-deep:#8fcfc9;
  --sand:#d8c596;
  --gold:#c9ae72;
  --light-text:#f2f2f2;
}
*{margin:0;padding:0;box-sizing:border-box}
html,body{width:1200px;height:775px;overflow:hidden;background:var(--stage)}
body{font-family:"Arimo",Arial,sans-serif;position:relative}
.card{position:absolute;width:492px;height:264px;overflow:hidden;box-shadow:0 3px 8px rgba(0,0,0,.35)}
.card--light{background:linear-gradient(135deg,var(--paper) 0%,var(--paper-shade) 100%)}
.card--dark{background:linear-gradient(135deg,var(--night-light) 0%,var(--night) 70%)}
.front-left{left:125px;top:108px}
.front-right{left:636px;top:108px}
.back-left{left:125px;top:403px}
.back-right{left:636px;top:403px}
.wave{position:absolute;left:0;top:0;width:492px;height:264px}
.flower-mark{position:absolute;border-radius:40% 60% 50% 50%}
.flower-mark--front{left:50px;top:26px;width:90px;height:70px;background:radial-gradient(circle,rgba(169,221,216,.75),rgba(201,174,114,.35) 70%,transparent 72%)}
.brand-name{position:absolute;left:34px;top:100px;font-weight:700;font-size:30px;color:var(--sea-deep);letter-spacing:.5px}
.card--dark .brand-name{color:var(--sea)}
.heading{position:absolute;right:18px;top:30px;text-align:right}
.heading__name{font-weight:700;font-size:17px;color:var(--ink)}
.heading__tag{font-weight:700;font-size:10.5px;color:var(--ink-soft);margin-top:2px}
.card--dark .heading__name,.card--dark .heading__tag{color:var(--light-text)}
.contact{position:absolute;right:18px;top:92px;text-align:right;font-size:8.6px;line-height:11.4px;color:var(--ink-soft);list-style:none}
.contact li.gap{margin-top:9px}
.card--dark .contact{right:14px;color:var(--light-text)}
.card--dark .contact li{padding-right:14px;position:relative}
.contact .dot{position:absolute;right:0;top:2px;width:8px;height:8px;border-radius:50%;background:var(--light-text)}
.flower-faint{position:absolute;left:55px;top:28px;width:150px;height:110px;border-radius:45%;background:radial-gradient(circle,rgba(201,174,114,.22),transparent 70%)}
.card--dark .flower-faint{background:radial-gradient(circle,rgba(150,150,150,.3),transparent 70%)}
.flower-gold{position:absolute;left:290px;top:28px;width:110px;height:100px;border-radius:45%;background:radial-gradient(circle,rgba(201,174,114,.45),transparent 70%)}
.web{position:absolute;right:18px;top:130px;font-size:15px;color:var(--ink)}
.card--dark .web{color:var(--light-text)}
</style>
</head>
<body>

<!-- Front, light -->
<section class="card card--light front-left">
  <svg class="wave" viewBox="0 0 492 264" aria-hidden="true">
    <path d="M0 212 C110 255 300 200 492 207 L492 264 L0 264Z" fill="var(--sea)"/>
    <path d="M0 205 C110 248 300 193 492 200" fill="none" stroke="var(--gold)" stroke-width="2"/>
  </svg>
  <div class="flower-mark flower-mark--front" role="img" aria-label="Orchid flower emblem"></div>
  <div class="brand-name">Saltmarsh</div>
  <header class="heading">
    <div class="heading__name">Saltmarsh Restaurant</div>
    <div class="heading__tag">Truly Island-Made</div>
  </header>
  <ul class="contact">
    <li>#41 Estate Coralind</li>
    <li>(at the Harbor Bluff Cottages)</li>
    <li>Christiansted, VI 00820</li>
    <li class="gap">340-555-0142</li>
    <li>340-555-0187/ 340-555-0163</li>
    <li>Saltmarsh_Restaurant@bayvistamail.com</li>
    <li>www.saltmarshvi-example.com</li>
  </ul>
</section>

<!-- Front, dark -->
<section class="card card--dark front-right">
  <svg class="wave" viewBox="0 0 492 264" aria-hidden="true">
    <path d="M0 200 C120 248 300 218 492 230 L492 264 L0 264Z" fill="var(--sand)"/>
    <path d="M0 193 C120 241 300 211 492 223" fill="none" stroke="var(--sea)" stroke-width="2.5"/>
  </svg>
  <div class="flower-mark flower-mark--front" role="img" aria-label="Orchid flower emblem"></div>
  <div class="brand-name">Saltmarsh</div>
  <header class="heading">
    <div class="heading__name">Saltmarsh Restaurant</div>
    <div class="heading__tag">Truly Island-Made</div>
  </header>
  <ul class="contact">
    <li>#41 Estate Coralind<span class="dot"></span></li>
    <li>(at the Harbor Bluff Cottages)</li>
    <li>Christiansted, VI 00820</li>
    <li class="gap">340-555-0142<span class="dot"></span></li>
    <li>340-555-0187/ 340-555-0163<span class="dot"></span></li>
    <li>Saltmarsh_Restaurant@bayvistamail.com<span class="dot"></span></li>
    <li>www.saltmarshvi-example.com<span class="dot"></span></li>
  </ul>
</section>

<!-- Back, light -->
<section class="card card--light back-left">
  <svg class="wave" viewBox="0 0 492 264" aria-hidden="true">
    <path d="M0 175 C120 235 320 205 492 215 L492 264 L0 264Z" fill="var(--sea)"/>
    <path d="M0 168 C120 228 320 198 492 208" fill="none" stroke="var(--gold)" stroke-width="2"/>
  </svg>
  <div class="flower-faint" role="img" aria-label="Faint orchid flower decoration"></div>
  <div class="flower-gold" role="img" aria-label="Gold orchid flower decoration"></div>
  <div class="web">www.saltmarshvi-example.com</div>
</section>

<!-- Back, dark -->
<section class="card card--dark back-right">
  <svg class="wave" viewBox="0 0 492 264" aria-hidden="true">
    <path d="M0 172 C120 232 320 200 492 210 L492 264 L0 264Z" fill="var(--sand)"/>
    <path d="M0 165 C120 225 320 193 492 203" fill="none" stroke="var(--sea)" stroke-width="2.5"/>
  </svg>
  <div class="flower-faint" role="img" aria-label="Faint grey orchid flower decoration"></div>
  <div class="flower-gold" role="img" aria-label="Gold orchid flower decoration"></div>
  <div class="web">www.saltmarshvi-example.com</div>
</section>

</body>
</html>
```